Branding pakage with new logo

Hi everyone, we just rebranded and i need a complete branding pakage that will flow together with everything.

Kvr 3400 vehicle wrap
Harlo pacer van wrap
2025 t480 wrap
16x8 enclosed trailer wrap
Business cards
Yard signs
Signage on building
Polo and t shirts for employees

Custom Window and door market

Window's doors and garage doors

```html
<!DOCTYPE html>
<html lang="en">
<head>
<meta charset="utf-8">
<title>Keystone Portals – Business Cards</title>
<link href="https://fonts.googleapis.com/css2?family=Open+Sans:wght@400;600;700;800&display=swap" rel="stylesheet">
<style>
  :root {
    --page: #e4e4e4;
    --orange: #e2531c;
    --rust-top: #b24c22;
    --rust-bottom: #3a2b26;
    --ink: #2a2a2a;
    --paper: #f7f7f6;
    --ghost: #e9e9e9;
    --card-black: #1f1e1d;
    --white: #ffffff;
  }
  * { margin: 0; padding: 0; box-sizing: border-box; }
  html, body {
    width: 1200px; height: 988px; overflow: hidden;
    background: var(--page);
    font-family: "Open Sans", Arial, sans-serif;
  }
  .canvas {
    position: relative; width: 1200px; height: 988px;
  }
  .card {
    position: absolute; left: 220px;
    width: 760px; height: 434px;
    border-radius: 30px; overflow: hidden;
    box-shadow: 0 6px 18px rgba(0,0,0,.18);
  }
  .card--front { top: 40px; background: var(--paper); }
  .card--back { top: 514px; background: var(--card-black); }

  /* front */
  .front__band {
    position: absolute; left: 245px; top: 0; width: 150px; height: 38px;
    background: var(--orange);
  }
  .front__bar {
    position: absolute; left: 30px; top: 105px; width: 95px; height: 329px;
    background: linear-gradient(180deg, var(--rust-top), var(--rust-bottom));
  }
  .front__ghost {
    position: absolute; right: 40px; top: 150px; width: 230px; height: 230px;
    background: var(--ghost);
  }
  .brand {
    position: absolute; left: 150px; top: 52px;
    display: flex; align-items: flex-end; gap: 14px;
  }
  .brand__square {
    width: 58px; height: 58px; background: var(--ink);
  }
  .brand__name {
    font-size: 30px; font-weight: 700; color: var(--orange);
    letter-spacing: .5px; line-height: 1;
  }
  .person {
    position: absolute; left: 150px; top: 140px;
  }
  .person__name {
    font-size: 34px; font-weight: 800; color: var(--ink); line-height: 1.1;
  }
  .person__role {
    display: flex; align-items: center; gap: 14px;
    font-size: 22px; font-weight: 700; color: var(--orange);
  }
  .person__rule {
    width: 200px; height: 1px; background: var(--orange); margin-top: 6px;
  }
  .contacts {
    position: absolute; left: 150px; top: 228px; list-style: none;
  }
  .contacts li {
    display: flex; align-items: center; gap: 12px;
    font-size: 17px; font-weight: 600; color: var(--ink); height: 32px;
  }
  .contacts svg { width: 18px; height: 18px; fill: var(--orange); flex: none; }

  /* back */
  .back__ghost {
    position: absolute; right: 40px; top: 170px; width: 230px; height: 230px;
    background: rgba(255,255,255,.05);
  }
  .back__brand {
    position: absolute; left: 90px; top: 150px;
    display: flex; align-items: flex-end; gap: 16px;
  }
  .back__square { width: 64px; height: 64px; background: var(--white); }
  .back__name {
    font-size: 36px; font-weight: 700; color: var(--white); line-height: 1; letter-spacing: .5px;
  }
  .back__url {
    position: absolute; left: 170px; top: 230px;
    font-size: 19px; font-weight: 600; color: var(--white); letter-spacing: 2px;
  }
</style>
</head>
<body>
<main class="canvas">
  <section class="card card--front" aria-label="Business card front">
    <div class="front__band"></div>
    <div class="front__bar"></div>
    <div class="front__ghost"></div>
    <div class="brand">
      <span class="brand__square"></span>
      <span class="brand__name">KEYSTONE PORTALS</span>
    </div>
    <div class="person">
      <p class="person__name">MILO HAVERLY</p>
      <p class="person__role">Manager <span class="person__rule"></span></p>
    </div>
    <ul class="contacts">
      <li><svg viewBox="0 0 24 24"><path d="M6.6 10.8a15.1 15.1 0 0 0 6.6 6.6l2.2-2.2c.3-.3.7-.4 1-.2 1.1.4 2.3.6 3.6.6.6 0 1 .4 1 1V20c0 .6-.4 1-1 1A17 17 0 0 1 3 4c0-.6.4-1 1-1h3.5c.6 0 1 .4 1 1 0 1.3.2 2.5.6 3.6.1.3 0 .7-.2 1z"/></svg>(555) 014-2270</li>
      <li><svg viewBox="0 0 24 24"><path d="M2 5h20v14H2zM4 7v.5l8 5 8-5V7l-8 5z"/></svg>keystoneportals@mail.com</li>
      <li><svg viewBox="0 0 24 24"><path d="M12 2a10 10 0 1 0 0 20 10 10 0 0 0 0-20zm6.9 6h-3a15 15 0 0 0-1.3-3.9A8 8 0 0 1 18.9 8zM12 4c.8 1.2 1.5 2.5 1.9 4h-3.8c.4-1.5 1.1-2.8 1.9-4zM4.3 14a8 8 0 0 1 0-4h3.4a16 16 0 0 0 0 4zm.8 2h3a15 15 0 0 0 1.3 3.9A8 8 0 0 1 5.1 16zm3-8h-3a8 8 0 0 1 4.3-3.9A15 15 0 0 0 8.1 8zM12 20c-.8-1.2-1.5-2.5-1.9-4h3.8c-.4 1.5-1.1 2.8-1.9 4zm2.3-6H9.7a14 14 0 0 1 0-4h4.6a14 14 0 0 1 0 4zm.3 5.9a15 15 0 0 0 1.3-3.9h3a8 8 0 0 1-4.3 3.9zm1.7-5.9a16 16 0 0 0 0-4h3.4a8 8 0 0 1 0 4z"/></svg>www.keystoneportals.org</li>
      <li><svg viewBox="0 0 24 24"><path d="M12 2a7 7 0 0 0-7 7c0 5.2 7 13 7 13s7-7.8 7-13a7 7 0 0 0-7-7zm0 9.5a2.5 2.5 0 1 1 0-5 2.5 2.5 0 0 1 0 5z"/></svg>42 Alder Ln, Maplecrest, Ontario K0A 1B3</li>
    </ul>
  </section>

  <section class="card card--back" aria-label="Business card back">
    <div class="back__ghost"></div>
    <div class="back__brand">
      <span class="back__square"></span>
      <span class="back__name">KEYSTONE PORTALS</span>
    </div>
    <p class="back__url">www.keystoneportals.org</p>
  </section>
</main>
</body>
</html>
```